Board Game Inspired Referral Tracker

Hello,

I'm looking to have a graphic designed on approximately 4 x 6 card stock or magnet. The graphic is essentially to be a board game. This is a 1 sided card.

It's a referral tracking system (for real estate). For each referral given that results in a closing the client will receive an incentive to keep referring.

I see it as:

1st referral: upon closing you receive $100
2nd referral: upon closing you receive $250
3rd referral: upon closing you receive $250
4th referral: upon closing you receive $250
5th referral: upon closing you receive $1000

I'm open for creativity, however I'd like it to reflect my branding (brightcornerhousestudio.example), include my logo but be very fun and somewhat interactive with cartoon-like inspiration (money bags/jackpot, bright colours, etc.). I'd like stickers to cover each referral box once it's been earned; they would have to be pre-cut / individual, these should be included in the design. I would like to see my logo incorporated in a creative way (see website for logo).

Ideally I'd like this to be ready to print by the end of this week, Friday, June 5th.

Looking forward to seeing your ideas!

Industry/Entity Type

Real Estate

Requirements
Must have
• My logo (Bright Corner House Studio)
• My brokerage logo (Marlowe Partners Realty) (small)
• "As a licensed Realtor®, my business thrives on trust and referrals from friends and family. I am pleased to offer you this generous incentive program for your support and enthusiasm.
• For each referral you send me that results in a successful closing, as a token of my gratitude, I will send you a gift certificate in the monetary amount indicated in the game below. Make it to five successful referrals and you’ll receive the jackpot!"
• Thank you for your support, and remember, I'm never too busy for your referrals.

```html
<!DOCTYPE html>
<html lang="en">
<head>
<meta charset="UTF-8">
<title>Referral Sticker – Thank You For Your Support</title>
<link href="https://fonts.googleapis.com/css2?family=Oswald:wght@600;700&family=Open+Sans:wght@300;700&display=swap" rel="stylesheet">
<style>
  :root {
    --ink-blue: #1f5a85;
    --text-dark: #3a3a3a;
    --text-mid: #555555;
    --paper: #ffffff;
    --vignette: #a9a9a9;
    --sticker-shade: #d9d9d9;
  }
  html, body {
    margin: 0;
    padding: 0;
    overflow: hidden;
  }
  .canvas {
    position: relative;
    width: 1200px;
    height: 729px;
    overflow: hidden;
    background: radial-gradient(ellipse 70% 68% at 50% 52%, var(--paper) 45%, #eeeeee 72%, var(--vignette) 100%);
  }
  .sticker {
    position: absolute;
    left: 165px;
    top: 172px;
    width: 394px;
    height: 394px;
    border-radius: 50%;
    box-sizing: border-box;
    border: 12px solid var(--ink-blue);
    background: radial-gradient(circle at 50% 45%, var(--paper) 40%, #f1f1f1 72%, var(--sticker-shade) 100%);
    box-shadow: 4px 6px 10px rgba(0, 0, 0, 0.35);
    display: flex;
    align-items: center;
    justify-content: center;
  }
  .sticker-message {
    margin: 0;
    font-family: "Oswald", "Arial Narrow", sans-serif;
    font-weight: 700;
    font-size: 66px;
    line-height: 56px;
    letter-spacing: 0.5px;
    color: var(--ink-blue);
    text-align: center;
    text-transform: uppercase;
    transform: rotate(-2deg) translate(-6px, 2px) scaleY(1.05);
  }
  .caption {
    position: absolute;
    left: 620px;
    top: 312px;
    font-family: "Open Sans", "Helvetica Neue", sans-serif;
    font-size: 34px;
    line-height: 40px;
  }
  .caption-title {
    margin: 0;
    font-weight: 700;
    color: var(--text-dark);
  }
  .caption-note {
    margin: 0;
    font-weight: 300;
    color: var(--text-mid);
  }
</style>
</head>
<body>
  <main class="canvas">
    <div class="sticker">
      <p class="sticker-message">Thank you<br>for your<br>support</p>
    </div>
    <div class="caption">
      <p class="caption-title">Sticker</p>
      <p class="caption-note">to cover each referral box</p>
    </div>
  </main>
</body>
</html>
```